Redesign Business Cards

I need the attached business cards redesigned. Multiple logo files attached. Please create a front and back to the business card. The front should have a white background. The back should have a black background.

The winner will be selected on the the following basis: professional look, both front and back of card included and each of the following elements included: phone, email, website, job title.

Thanks in advance for your help!!!!

```html
<!DOCTYPE html>
<html lang="en">
<head>
<meta charset="utf-8">
<title>PetroShift Business Cards</title>
<link rel="stylesheet" href="https://fonts.googleapis.com/css2?family=Source+Sans+3:wght@300;400;600;700;800&display=swap">
<style>
  :root {
    --backdrop: #e4e2df;
    --card-white: #ffffff;
    --card-black: #0b0b0b;
    --ink: #1c1c1c;
    --ink-soft: #3a3a3a;
    --logo-grey: #2e2e2e;
    --paper-text: #f2f2f2;
  }
  * { margin: 0; padding: 0; box-sizing: border-box; }
  html, body { width: 1200px; height: 795px; overflow: hidden; }
  body {
    background: var(--backdrop);
    font-family: "Source Sans 3", "Myriad Pro", sans-serif;
    position: relative;
  }
  .card {
    position: absolute;
    width: 540px;
    height: 309px;
    overflow: hidden;
    box-shadow: 0 6px 18px rgba(0,0,0,0.25);
  }
  /* ---------- Front ---------- */
  .card--front { left: 190px; top: 60px; background: var(--card-white); color: var(--ink); }
  .front-brand {
    position: absolute;
    left: 20px;
    top: 293px;
    width: 277px;
    transform: rotate(-90deg);
    transform-origin: top left;
    display: flex;
    flex-direction: column;
    align-items: center;
    gap: 4px;
    white-space: nowrap;
  }
  .front-brand__name {
    font-weight: 800;
    font-size: 36px;
    line-height: 1;
    color: var(--logo-grey);
    display: flex;
    align-items: center;
    gap: 8px;
  }
  .front-brand__dot {
    width: 20px; height: 20px;
    border-radius: 50%;
    background: var(--logo-grey);
  }
  .front-brand__descriptor {
    font-weight: 300;
    font-size: 17px;
    line-height: 1.2;
    color: var(--ink-soft);
  }
  .front-tagline {
    position: absolute;
    left: 200px; top: 24px;
    font-weight: 600;
    font-size: 13.5px;
    color: var(--ink);
  }
  .front-person { position: absolute; left: 198px; top: 92px; }
  .front-person__name { font-weight: 700; font-size: 26px; line-height: 1.1; }
  .front-person__title { font-weight: 400; font-size: 20px; line-height: 1.3; }
  .front-contact {
    position: absolute;
    left: 198px; top: 210px;
    list-style: none;
    font-weight: 400;
    font-size: 19px;
    line-height: 1.4;
    color: var(--ink-soft);
  }
  /* ---------- Back ---------- */
  .card--back {
    left: 500px; top: 420px;
    background: var(--card-black);
    color: var(--paper-text);
    display: flex;
    flex-direction: column;
    align-items: center;
    justify-content: center;
    gap: 18px;
  }
  .back-brand {
    display: flex;
    align-items: center;
    gap: 14px;
    font-weight: 800;
    font-size: 66px;
    line-height: 1;
    letter-spacing: 1px;
    white-space: nowrap;
  }
  .back-brand__dot {
    width: 36px; height: 36px;
    border-radius: 50%;
    background: var(--paper-text);
  }
  .back-tagline { font-weight: 300; font-size: 19px; }
</style>
</head>
<body>
  <section class="card card--front" aria-label="Business card front">
    <div class="front-brand">
      <div class="front-brand__name"><span class="front-brand__dot"></span>PETROSHIFT</div>
      <div class="front-brand__descriptor">Oil and Gas Change Management</div>
    </div>
    <p class="front-tagline">Project and Change Management for Oil Companies</p>
    <div class="front-person">
      <p class="front-person__name">John Doe</p>
      <p class="front-person__title">Managing Partner</p>
    </div>
    <ul class="front-contact">
      <li>www.PetroShift.com</li>
      <li>p.555.xxx.xxxx</li>
      <li>e.XXxxxx@PetroShift.com</li>
    </ul>
  </section>

  <section class="card card--back" aria-label="Business card back">
    <div class="back-brand"><span class="back-brand__dot"></span>PETROSHIFT</div>
    <p class="back-tagline">Project and Change Management for Oil Companies</p>
  </section>
</body>
</html>
```